Werbe Flyer an Hausbesitzer
Zielgruppe
Wir sind ein Immobilien Makler in Zürich. Wir werden den Werbe-Flyer zusammen mit einem Begleitschreiben und einem Rückantwort-Briefumschlag an Hausbesitzer per Post senden.
Zielgruppe:
ältere Leute, die Ihr Haus oder Wohnung verkaufen möchten.
Ziel:
Wir möchten den Maklerauftrag bekommen
Aufgabenstellung
Ein Werbe-Flyer erstellen.
Format:
A5
4 Seiten (Also A4 quer einmal gefaltet)
Hochformat
ein Beispiel liegt bei.
Der Text ist bereits definitiv.
Bilder und Layout ist frei wählbar.
Letzte Seite sollte abgetrennt werden können für die Rücksendung
Unsere Webpage als Info evtl. für Layout:
www.velaro-haus.ch

```html
<!DOCTYPE html>
<html lang="de">
<head>
<meta charset="utf-8">
<title>Velaro Haus AG – Flyer</title>
<link rel="stylesheet" href="https://fonts.googleapis.com/css2?family=Lato:wght@300;400;700&family=PT+Sans+Narrow&family=PT+Sans:ital@1&display=swap">
<style>
  :root {
    --stage: #6f6f6f;
    --paper: #ffffff;
    --band-top: #d6d6d6;
    --band-bottom: #f4f4f4;
    --navy: #1d3a5e;
    --blue: #2b5d9b;
    --accent: #35b4d2;
    --ink: #2a2a2a;
    --rule: #8a8a8a;
  }
  * { box-sizing: border-box; margin: 0; padding: 0; }
  html, body { width: 915px; height: 1200px; overflow: hidden; }
  body { background: var(--stage); font-family: "Lato", sans-serif; color: var(--ink); position: relative; }

  .spread { position: absolute; left: 65px; width: 777px; height: 549px; background: var(--paper);
            box-shadow: 3px 4px 8px rgba(0,0,0,.45); overflow: hidden; }
  .spread--outer { top: 35px; }
  .spread--inner { top: 620px; }
  .band { position: absolute; left: 0; width: 100%;
          background: linear-gradient(180deg, var(--band-top), var(--band-bottom)); }
  .band--head { top: 0; height: 118px; }
  .band--foot { bottom: 0; height: 51px; background: linear-gradient(180deg, #f2f2f2, #d4d4d4); }
  .abs { position: absolute; }

  .brand { position: absolute; top: 30px; display: flex; align-items: center; gap: 7px; }
  .brand__mark { width: 24px; height: 24px; background: var(--navy); }
  .brand__name { font-size: 28px; font-weight: 400; letter-spacing: 2px; color: var(--navy); line-height: 1; }

  .fold { position: absolute; left: 384px; top: 0; width: 1px; height: 118px; background: #c4c4c4; }

  .reply__title { left: 39px; top: 131px; font-size: 11px; color: var(--blue); }
  .reply__text { left: 81px; font-size: 9.2px; }
  .reply__strong { font-weight: 700; }
  .checkbox { position: absolute; left: 81px; width: 16px; height: 16px; border: 1px solid #9a9a9a; }
  .option { position: absolute; left: 104px; font-size: 9.8px; }
  .field { position: absolute; left: 81px; width: 279px; border-top: 1px solid var(--rule);
           font-size: 9px; padding-top: 3px; }
  .reply__address { left: 81px; top: 507px; font-size: 9.4px; line-height: 12.5px; }
  .scissors { left: 373px; top: 512px; }

  .cover__scene { left: 388px; top: 118px; width: 389px; height: 431px;
     background: linear-gradient(180deg, #2f6aad 0%, #4f86c0 35%, #7f95a4 52%, #5f7e45 70%, #4e6a2e 100%); }
  .photo { position: absolute; left: 611px; width: 147px; border: 1px solid #fff; }
  .photo--loft { top: 69px; height: 101px; background: linear-gradient(135deg, #e9e9e6, #b9b3a6); }
  .photo--chalet { top: 172px; height: 110px; background: linear-gradient(180deg, #9cc2e2, #e8e6df 50%, #5f8d3d); }
  .photo--house { top: 286px; height: 105px; background: linear-gradient(180deg, #8fb3d8, #f1f1ef 55%, #6c8a45); }
  .photo--block { top: 392px; height: 80px; background: linear-gradient(180deg, #dfe8ee, #8a9a7c 60%, #6b7c55); }
  .cover__claim { left: 418px; top: 422px; font-size: 20px; font-weight: 300; line-height: 24px; color: #fff; }
  .cover__url { left: 611px; top: 505px; font-size: 14.5px; font-weight: 700; color: #fff; }

  .contact { left: 472px; top: 34px; font-size: 10px; line-height: 13.6px; }
  .photo--office { top: 22px; height: 111px; background: linear-gradient(180deg, #d5d7d8, #6d5a48 45%, #8a8378); }
  .partner__title { left: 79px; top: 133px; font-size: 12px; line-height: 15.5px; font-weight: 400; }
  .team__scene { left: 0; top: 166px; width: 470px; height: 332px;
     background: linear-gradient(90deg, rgba(160,176,195,.9), rgba(196,206,218,.6) 70%, rgba(255,255,255,0)); }
  .team__portrait { left: 108px; top: 171px; width: 244px; height: 327px;
     background: linear-gradient(180deg, #c9cfd6, #2e2e33 45%, #1f1f24); }
  .quote { left: 33px; top: 186px; font-family: "PT Sans", sans-serif; font-style: italic;
           font-size: 14.5px; line-height: 18.5px; color: var(--navy); }
  .service__head { left: 418px; font-size: 10.6px; color: var(--blue); }
  .service__body { left: 472px; width: 275px; font-size: 8.9px; line-height: 12.2px; }
  .consultants { left: 39px; top: 504px; font-size: 9.2px; }
  .consultant { top: 504px; font-size: 9.2px; line-height: 12px; }
  .consultant__name { color: var(--blue); font-size: 10px; }
</style>
</head>
<body>

<section class="spread spread--outer">
  <div class="band band--head"></div>
  <div class="fold"></div>

  <div class="brand" style="left:40px"><span class="brand__mark"></span><span class="brand__name">VELARO</span></div>
  <div class="brand" style="left:418px"><span class="brand__mark"></span><span class="brand__name">VELARO</span></div>

  <h2 class="abs reply__title">RÜCKANTWORT</h2>
  <p class="abs reply__text" style="top:152px">Einfach abtrennen und im beigefügten Rückumschlag an uns senden</p>
  <p class="abs reply__text reply__strong" style="top:176px">Bitte kreuzen Sie Ihre Wünsche an.</p>
  <p class="abs reply__text reply__strong" style="top:202px">Ja, wir möchten …</p>

  <span class="checkbox" style="top:228px"></span><span class="option" style="top:235px">… unsere Immobilie verkaufen</span>
  <span class="checkbox" style="top:260px"></span><span class="option" style="top:267px">… eine Immobilie kaufen</span>
  <span class="checkbox" style="top:293px"></span><span class="option" style="top:300px">… ein persönliches Gespräch</span>

  <div class="field" style="top:344px">Name/Vorname</div>
  <div class="field" style="top:375px">Strasse</div>
  <div class="field" style="top:407px">PLZ/Ort</div>
  <div class="field" style="top:439px">Telefon</div>
  <div class="field" style="top:470px">E-Mail</div>

  <p class="abs reply__address">VELARO HAUS AG | LINDENWEG 12 | 8008 ZÜRICH<br>Fax 044 600 12 35 | info@velaro-haus.ch | www.velaro-haus.ch</p>

  <svg class="abs scissors" width="14" height="20" viewBox="0 0 14 20" aria-hidden="true">
    <g fill="none" stroke="#444" stroke-width="1">
      <circle cx="3.5" cy="16" r="2.4"/><circle cx="10.5" cy="16" r="2.4"/>
      <path d="M5 14 L9.5 1 M9 14 L6 5"/>
    </g>
  </svg>

  <div class="abs cover__scene" role="img" aria-label="Alpenlandschaft mit blauem Himmel und Blumenwiese"></div>
  <div class="photo photo--loft" role="img" aria-label="Helle Dachwohnung mit grossen Fenstern"></div>
  <div class="photo photo--chalet" role="img" aria-label="Einfamilienhaus mit Garten"></div>
  <div class="photo photo--house" role="img" aria-label="Neues weisses Einfamilienhaus"></div>
  <div class="photo photo--block" role="img" aria-label="Begrünte Mehrfamilienhäuser"></div>

  <h1 class="abs cover__claim">IMMOBILIEN<br>SIND UNSERE<br>LEIDENSCHAFT</h1>
  <p class="abs cover__url">www.velaro-haus.ch</p>
</section>

<section class="spread spread--inner">
  <div class="band band--head"></div>
  <div class="band band--foot"></div>

  <div class="brand" style="left:40px"><span class="brand__mark"></span><span class="brand__name">VELARO</span></div>

  <address class="abs contact" style="font-style:normal">VELARO HAUS AG<br>Lindenweg 12<br>8008 Zürich<br>Tel. 044 600 12 30<br>Fax 044 600 12 35<br>info@velaro-haus.ch</address>
  <div class="photo photo--office" role="img" aria-label="Bürogebäude mit Holzfassade"></div>

  <h2 class="abs partner__title">IHRE PARTNER FÜR ALLE FRAGEN<br>RUND UM IHRE IMMOBILIE</h2>

  <div class="abs team__scene" role="img" aria-label="Zürcher Altstadt am See vor verschneiten Bergen"></div>
  <div class="abs team__portrait" role="img" aria-label="Die beiden Berater im Anzug"></div>
  <p class="abs quote">„Wir setzen uns für<br>&nbsp;jede Liegenschaft<br>&nbsp;ein, als wäre es<br>&nbsp;unsere Eigene.“</p>

  <h3 class="abs service__head" style="top:133px">UNSERE DIENSTLEISTUNGEN</h3>
  <p class="abs service__body" style="top:151px">Der Kauf und Verkauf von Immobilien ist Vertrauenssache. Aus diesem Grund geniesst bei Velaro Haus AG die persönliche Beziehung zum Kunden neben allen fachlichen Aspekten in jeder Phase höchste Priorität. So behalten Sie stets den Überblick und bleiben in jeder Phase auf dem Laufenden.</p>

  <h3 class="abs service__head" style="top:226px">SCHÄTZUNG</h3>
  <p class="abs service__body" style="top:245px">Es gibt viele Gründe, sich auch ohne Verkaufsabsichten hin und wieder über den Wert seiner eigenen Immobilie zu informieren. Wir übernehmen für Sie auf Wunsch die genaue und objektive Wertbeurteilung von Einfamilienhaus und Grundstück.</p>

  <h3 class="abs service__head" style="top:308px">VERKAUF</h3>
  <p class="abs service__body" style="top:327px">Ist ein Verkauf geplant, überprüfen wir für Sie im Vorfeld die aktuellen Verkaufsmöglichkeiten. Dazu gehören sowohl die Ermittlung eines realistischen Verkaufspreises als auch die Erstellung detaillierter Verkaufsunterlagen. Auch Objektbesichtigungen führen wir für Sie durch.</p>

  <h3 class="abs service__head" style="top:404px">BEURKUNDUNG UND ÜBERTRAGUNG</h3>
  <p class="abs service__body" style="top:422px">Neben Schätzung Ihrer Liegenschaft und Marketing führen wir für Sie auch die Preisverhandlungen mit potentiellen Interessenten. Zudem erstellen wir mit dem zuständigen Notariat den Entwurf und die Ausarbeitung der Kaufverträge und begleiten Sie bis zur Beurkundung und Eigentumsübertragung auf dem Grundbuchamt.</p>

  <p class="abs consultants">The creative consultants</p>
  <p class="abs consultant" style="left:146px"><span class="consultant__name">MARC-ANDRÉ KELLER</span><br>Tel. direkt 044 600 12 34</p>
  <p class="abs consultant" style="left:262px"><span class="consultant__name">PETER B. STAUB</span><br>Tel. direkt 044 600 12 30</p>
</section>

</body>
</html>
```